Webdesign für Projektmanagement
Zielgruppe
Projektmanagement und Projektsteuerung von Bauvorhaben für Projektentwickler und Bauträger.
Wesentliche Bereiche sind Wirtschaftliche Steuerung, Steuerung der Baustelle und Bauabläufe sowie Steuerung der Marketing und Vertriebsaktivitäten.
Aufgabenstellung
Orientierung am Logo. Logo und Visitenkarte liegen bei. Schriftart Prelo und Prelo Slab.

```html
<!DOCTYPE html>
<html lang="de">
<head>
<meta charset="utf-8">
<title>Veldkamp – Projektmanagement und Projektsteuerung</title>
<link rel="stylesheet" href="https://fonts.googleapis.com/css2?family=Zilla+Slab:wght@400;500;600;700&family=Fira+Sans:ital,wght@0,300;0,400;0,500;1,300;1,400&display=swap">
<style>
  :root{
    --navy:#0b2540;
    --navy-deep:#032340;
    --gold:#a8924a;
    --text:#4a4f57;
    --muted:#9aa0a8;
    --white:#ffffff;
  }
  *{box-sizing:border-box;margin:0;padding:0}
  html,body{width:1200px;height:3629px;overflow:hidden;background:var(--white)}
  body{position:relative;font-family:"Fira Sans",sans-serif;color:var(--text)}
  .abs{position:absolute}
  .front{z-index:2}

  /* header */
  .brand{left:57px;top:56px;font-family:"Zilla Slab",serif;font-weight:700;font-size:38px;color:var(--navy)}
  .nav{right:68px;top:66px;display:flex;gap:30px;font-size:18px;color:var(--muted);font-weight:300}
  .nav a{color:inherit;text-decoration:none}
  .nav a.active{color:var(--navy);font-weight:400}

  /* hero */
  .hero-title{left:130px;top:208px;width:540px;font-family:"Zilla Slab",serif;font-weight:500;font-size:34px;line-height:42px;color:var(--navy)}
  .hero-sub{left:130px;top:352px;white-space:nowrap;font-style:italic;font-weight:300;font-size:21px;color:var(--gold)}
  .hero-art{left:590px;top:260px;width:610px;height:270px;background:linear-gradient(90deg,#ffffff 0%,#f3f1ea 35%,#ebe6d4 100%)}
  .hero-line{left:435px;top:533px;width:765px;height:6px;background:var(--gold)}

  /* consulting */
  .consult-title{left:130px;top:664px;font-family:"Zilla Slab",serif;font-weight:500;font-size:34px;line-height:40px;color:var(--navy)}
  .btn-gold{left:155px;top:768px;width:147px;height:37px;border-radius:19px;background:var(--gold);color:#fff;font-size:12.5px;display:flex;align-items:center;justify-content:center;box-shadow:0 10px 18px rgba(168,146,74,.35)}
  .consult-text{left:610px;top:668px;width:440px;font-size:14.5px;line-height:28px;font-weight:300;color:var(--text)}
  .consult-text p{margin-bottom:16px}

  /* intro band */
  .band{left:0;top:1090px;width:1200px;height:520px;background:linear-gradient(180deg,#e9e9e9 0%,#ffffff 14%,#ffffff 70%,#f1f1f1 100%)}
  .intro{left:348px;top:1228px;width:520px;font-family:"Zilla Slab",serif;font-weight:400;font-size:21px;line-height:33.5px;color:#3d4652}
  .skyline{left:315px;top:1458px;width:615px;height:150px;background:linear-gradient(180deg,#f6f4ee 0%,#e8e3d2 100%)}
  .ground{left:0;top:1607px;width:1200px;height:6px;background:var(--gold)}

  /* services */
  .services-title{left:131px;top:1722px;font-family:"Zilla Slab",serif;font-weight:500;font-size:30px;color:var(--navy)}
  .tabs{left:132px;top:1802px;display:flex;gap:58px;font-size:20px;font-weight:300;color:#b5b9bf}
  .tabs .on{color:var(--navy);font-weight:400}
  .photo-house{background:linear-gradient(135deg,#d9d4c9 0%,#f1ede4 45%,#9a8a6e 100%)}
  .photo-city{background:linear-gradient(180deg,#3f4e6a 0%,#2d3548 55%,#1d2230 100%)}
  .card{background:#fff;box-shadow:0 18px 30px rgba(0,0,0,.06);padding:30px 35px}
  .card h3{font-family:"Zilla Slab",serif;font-weight:700;font-size:13px;color:#222;margin-bottom:6px}
  .card .addr{font-family:"Zilla Slab",serif;font-size:12px;color:var(--gold);margin-bottom:22px}
  .card p{font-size:14.5px;line-height:21px;font-weight:300;color:#333}

  /* career */
  .career{left:0;top:2307px;width:1200px;height:553px;background:var(--navy-deep)}
  .career-title{left:128px;top:2430px;font-family:"Zilla Slab",serif;font-weight:500;font-size:30px;color:#fff}
  .career-sub{left:128px;top:2472px;font-style:italic;font-weight:300;font-size:21px;color:var(--gold)}
  .career-text{left:128px;top:2532px;width:325px;font-size:15px;line-height:28px;font-weight:300;color:#c9d2dc}
  .btn-outline{left:128px;top:2685px;width:150px;height:36px;border:1px solid #7e8ea0;color:#fff;font-size:13px;letter-spacing:1px;display:flex;align-items:center;justify-content:center}
  .handshake{left:573px;top:2430px;width:627px;height:432px;background:linear-gradient(120deg,#e9f0f4 0%,#c7d7e0 45%,#b89a82 60%,#9fb6c6 100%)}

  /* map */
  .map{left:0;top:2858px;width:1200px;height:368px;background:linear-gradient(180deg,#ececec 0%,#e3e3e3 100%)}
  .pin{left:560px;top:3090px}

  /* location */
  .loc-title{left:128px;top:3312px;font-family:"Zilla Slab",serif;font-weight:500;font-size:30px;color:var(--navy)}
  .loc-addr{left:757px;top:3322px;font-size:15px;line-height:25.5px;color:var(--navy);font-weight:300;font-style:normal}
  .loc-addr strong{font-weight:500}
</style>
</head>
<body>

<header>
  <div class="abs brand">Veldkamp</div>
  <nav class="abs nav">
    <a class="active" href="#">Home</a>
    <a href="#">Leistungen</a>
    <a href="#">Referenzen</a>
    <a href="#">Über Uns</a>
    <a href="#">Kontakt</a>
  </nav>
</header>

<section class="hero">
  <div class="abs hero-art" role="img" aria-label="Linienillustration eines Hochhauses mit Nebengebäuden und einem Baum auf einem Raster"></div>
  <div class="abs hero-line"></div>
  <h1 class="abs front hero-title">Projektmanagement und<br>Projektsteuerung von<br>Bauvorhaben</h1>
  <p class="abs front hero-sub">für Projektentwickler und Bauträger</p>
</section>

<section class="consult">
  <h2 class="abs consult-title">Ganzheitliche<br>Beratung</h2>
  <div class="abs btn-gold">Jetzt beraten lassen</div>
  <div class="abs consult-text">
    <p>Die zunehmende Urbanisierung hat den Immobilienmarkt in den letzten Jahren nachhaltig verändert. Als Teil des größten Ballungszentrums Europas, hat dies starke Auswirkungen auf die Metropolregion Köln, Düsseldorf und Bonn. Begleitet wird diese Entwicklung durch vielschichtige städtebauliche Maßnahmen in der Region.</p>
    <p>Die Konsequenz aus dieser Entwicklung ist ein hoher Investitions-, Umnutzungs- und Projektentwicklungsbedarf bei Immobilien. Daraus entstanden ist ein für Investoren strukturell attraktiver Markt.</p>
  </div>
</section>

<section class="intro-band">
  <div class="abs band"></div>
  <p class="abs intro">Wir sind ein interdisziplinär tätiges, mittelständisches Beratungs- und Dienstleistungsunternehmen. Wir bieten unseren Kunden maßgeschneiderte Dienstleistungen für ihr Immobilienportfolios an.</p>
  <div class="abs skyline" role="img" aria-label="Linienillustration einer Stadtsilhouette mit Bäumen und goldener Sonne"></div>
  <div class="abs ground"></div>
</section>

<section class="services">
  <h2 class="abs services-title">Unsere Leistungen</h2>
  <div class="abs tabs">
    <span class="on">Immobiliensanierung</span>
    <span>Immobilienmanagement</span>
    <span>Immobilienvertrieb und -marketing</span>
  </div>

  <div class="abs photo-house" style="left:0;top:1912px;width:75px;height:245px" role="img" aria-label="Foto eines weißen Wohnhauses"></div>
  <article class="abs card" style="left:75px;top:1912px;width:337px;height:245px">
    <h3>Harbour Row One</h3>
    <div class="addr">24 Quay Lane, Northbay</div>
    <p>Harbour Row is a new pocket neighbourhood where considered apartment living meets shared green spaces in one of Riverton's oldest urban villages. To be developed over two stages, it will comprise 239 apartments.</p>
  </article>

  <div class="abs photo-house" style="left:412px;top:1912px;width:212px;height:245px" role="img" aria-label="Foto eines weißen Wohnhauses mit Garage"></div>
  <article class="abs card" style="left:624px;top:1912px;width:335px;height:245px">
    <h3>Harbour Row One</h3>
    <div class="addr">24 Quay Lane, Northbay</div>
    <p>Harbour Row is a new pocket neighbourhood where considered apartment living meets shared green spaces in one of Riverton's oldest urban villages. To be developed over two stages, it will comprise 239 apartments.</p>
  </article>

  <div class="abs photo-city" style="left:959px;top:1912px;width:189px;height:245px" role="img" aria-label="Foto einer Stadt in der Abenddämmerung"></div>
  <article class="abs card" style="left:1148px;top:1912px;width:52px;height:245px"></article>
</section>

<section class="career-section">
  <div class="abs career"></div>
  <h2 class="abs career-title">Karriere bei Veldkamp</h2>
  <p class="abs career-sub">wir suchen Verstärkung</p>
  <p class="abs career-text">Wir sind ständig auf der Suche nach qualifizierten Mitarbeiterinnen und Mitarbeitern um unser Team von 60 Mitarbeitern weiter zu verstärken.</p>
  <div class="abs btn-outline">JETZT BEWERBEN</div>
  <div class="abs handshake" role="img" aria-label="Foto eines Händedrucks zweier Geschäftsleute"></div>
</section>

<section class="location">
  <div class="abs map" role="img" aria-label="Karte der Region Düsseldorf mit Standortmarkierung"></div>
  <svg class="abs pin" width="40" height="56" viewBox="0 0 40 56" aria-hidden="true">
    <path d="M20 2C10 2 2 10 2 20c0 13 18 34 18 34s18-21 18-34C38 10 30 2 20 2z" fill="#a8924a"/>
    <circle cx="20" cy="20" r="7" fill="#fff"/>
  </svg>
  <h2 class="abs loc-title">Unser Standort</h2>
  <address class="abs loc-addr">
    <strong>Veldkamp Real Estate GmbH</strong><br>
    Lindenhofstr. 14<br>
    40210 Düsseldorf<br>
    Tel: +49(0)211 - 55501230<br>
    Fax: +49(0)211 - 555012399<br>
    E-Mail: info@veldkamp-re.de
  </address>
</section>

</body>
</html>
```